Vasko Lumen Entertainment

I need a web design for my Business for better online promotions and services.. The name of my company is Vasko Lumen its a entertainment company music, events, networking and so on.. What I do is help artist create and finish projects such as mix tapes, music videos, and book performances in order to create a platform and i also offer representation to help grow there brands or business... I also work with and help develop independent artists!!!

Target Market(s)

Hip hop and R&B industry

Industry/Entity Type

Entertainment Industry

Number of Pages Required

1 page

Requirements
Must have
• Must display My previous and upcoming work i want people to see the quality I provide in my service.. I have more videos that I want to upload on there to show more work.... I would like to bring all the separate promotions and campaigns that I previously had and currently have all one platform for everybody to see and to find more easily instead having everything so spread out..
Nice to have
• Creativity thats going to compliment my work and quality..

```html
<!DOCTYPE html>
<html lang="en">
<head>
<meta charset="utf-8">
<title>Vasko Lumen Entertainment</title>
<link href="https://fonts.googleapis.com/css2?family=Roboto+Slab:wght@300;400;700&family=Open+Sans:wght@400;600;700&display=swap" rel="stylesheet">
<style>
:root{
  --red:#c8161e;
  --ink:#333333;
  --muted:#6f6f6f;
  --grey-circle:#6b6b6b;
  --header:#151515;
  --footer:#1c1c1c;
  --studio-bg:#f5f6f8;
  --line:#e3e3e3;
  --silver:#d9dcdf;
  --white:#ffffff;
}
*{margin:0;padding:0;box-sizing:border-box}
html,body{width:1200px;height:2826px;overflow:hidden;background:var(--white)}
body{position:relative;font-family:"Open Sans",Arial,sans-serif;color:var(--ink)}
.abs{position:absolute}
.slab{font-family:"Roboto Slab",Georgia,serif}

/* header */
.site-header{left:0;top:0;width:1200px;height:94px;background:var(--header);border-bottom:3px solid var(--red)}
.brand{left:86px;top:24px;display:flex;align-items:center;gap:10px}
.brand-mark{width:18px;height:18px;background:var(--red)}
.brand-name{font-family:"Roboto Slab",Georgia,serif;font-size:22px;font-weight:400;color:var(--red);letter-spacing:1px}
.main-nav{top:42px;left:0;width:1200px;height:20px}
.main-nav a{position:absolute;font-family:"Roboto Slab",Georgia,serif;font-size:12px;color:#e6e6e6;text-decoration:none;letter-spacing:.5px}
.main-nav a.active{color:var(--red)}

/* hero */
.hero{left:0;top:94px;width:1200px;height:663px;background:
  radial-gradient(ellipse 260px 220px at 50% 52%,rgba(60,170,60,.55) 0%,rgba(30,90,30,.2) 60%,rgba(0,0,0,0) 100%),
  radial-gradient(ellipse at 50% 40%,#23482a 0%,#16301a 40%,#0c160e 75%,#070a08 100%)}
.hero-art{left:0;top:0;width:1200px;height:663px}
.hero-title{left:0;top:70px;width:1200px;text-align:center;font-family:"Roboto Slab",Georgia,serif;font-weight:700;font-size:74px;line-height:1;color:var(--silver);letter-spacing:1px;text-shadow:0 4px 10px rgba(0,0,0,.7)}
.hero-arrow{width:50px;height:50px;border:2px solid #fff;border-radius:50%;top:308px;display:flex;align-items:center;justify-content:center}

/* welcome */
.welcome-title{top:790px;left:0;width:1200px;text-align:center;font-size:26px;font-weight:300;color:#555}
.welcome-title span{color:var(--red);font-weight:400}
.welcome-sub{top:838px;left:0;width:1200px;text-align:center;font-size:12px;color:var(--muted)}
.service{width:330px;text-align:center}
.service-icon{width:116px;height:116px;border-radius:50%;background:var(--grey-circle);margin:0 auto;display:flex;align-items:center;justify-content:center}
.service-icon.is-red{background:var(--red)}
.service-name{font-family:"Roboto Slab",Georgia,serif;font-size:21px;font-weight:300;color:#555;margin-top:24px}
.service-name.is-red{color:var(--red);font-weight:400}
.service-text{font-size:12px;line-height:25px;color:var(--muted);margin-top:10px}

/* studio */
.studio{left:0;top:1187px;width:1200px;height:480px;background:var(--studio-bg)}
.section-title{font-family:"Roboto Slab",Georgia,serif;font-size:27px;font-weight:300;color:#555}
.section-title span{color:var(--red);font-weight:400}
.mini-arrow{width:30px;height:30px;border:1px solid #cfcfcf;border-radius:50%;display:flex;align-items:center;justify-content:center;background:#fff}
.session{left:87px;width:1026px;height:158px;background:#fff;border:1px solid var(--line);border-radius:3px}
.session-date{left:0;top:28px;width:128px;text-align:center}
.session-day{font-family:"Roboto Slab",Georgia,serif;font-size:52px;font-weight:300;color:#555;line-height:60px}
.session-month{font-family:"Roboto Slab",Georgia,serif;font-size:14px;font-weight:300;color:#555;margin-top:6px}
.divider-v{width:1px;top:28px;height:102px;background:var(--line)}
.session-thumb{left:147px;top:40px;width:83px;height:78px;background:linear-gradient(135deg,#5a4a3a,#2a1f1a 60%,#6a2a3a)}
.session-title{left:248px;top:44px;font-family:"Roboto Slab",Georgia,serif;font-size:16px;font-weight:400;color:#333}
.session-text{left:248px;top:78px;width:230px;font-size:12px;line-height:24px;color:var(--muted)}
.wave{left:531px;top:52px}
.ticket-label{left:791px;top:48px;font-family:"Roboto Slab",Georgia,serif;font-size:14px;font-weight:300;color:#666}
.ticket-price{left:791px;top:74px;font-family:"Roboto Slab",Georgia,serif;font-size:36px;font-weight:400;color:var(--red)}
.btn-details{left:896px;top:66px;width:108px;height:36px;background:var(--red);color:#fff;font-size:11px;font-weight:600;display:flex;align-items:center;justify-content:center;border-radius:2px}

/* promo */
.promo{left:0;top:1667px;width:1200px;height:319px;background:linear-gradient(100deg,#1e1a18 0%,#3a2a22 40%,#2a1e1a 65%,#4a2a28 85%,#1c1816 100%)}
.promo-title{top:84px;left:0;width:1200px;text-align:center;font-family:"Roboto Slab",Georgia,serif;font-size:28px;font-weight:400;color:#fff}
.promo-text{top:136px;left:240px;width:720px;text-align:center;font-size:12px;line-height:26px;color:#f0f0f0}
.btn-outline{left:488px;top:208px;width:226px;height:41px;border:1px solid #d8d8d8;border-radius:3px;color:#fff;font-family:"Roboto Slab",Georgia,serif;font-size:16px;display:flex;align-items:center;justify-content:center}

/* featured video */
.video-copy{left:87px;width:460px;font-size:12px;line-height:20.5px;color:var(--muted)}
.btn-red{left:87px;top:2302px;width:171px;height:44px;background:var(--red);color:#fff;border-radius:3px;font-family:"Roboto Slab",Georgia,serif;font-size:15px;display:flex;align-items:center;justify-content:center}
.video-frame{left:618px;top:2033px;width:495px;height:303px;background:radial-gradient(ellipse at 50% 45%,#b0621e 0%,#6a3414 45%,#2a140a 100%)}
.play{left:216px;top:130px;width:60px;height:44px;background:var(--red);border-radius:9px;display:flex;align-items:center;justify-content:center}

/* partners */
.partners{left:0;top:2400px;width:1200px;height:117px;background:var(--red)}
.partner{top:21px;width:141px;height:77px;border:1px solid rgba(255,255,255,.45);display:flex;align-items:center;justify-content:center}
.partner-shape{width:88px;height:20px;background:rgba(255,255,255,.85);border-radius:3px}

/* footer */
.site-footer{left:0;top:2517px;width:1200px;height:309px;background:var(--footer);color:#e8e8e8}
.footer-brand{left:118px;top:112px;display:flex;align-items:center;gap:12px}
.footer-brand .brand-mark{width:22px;height:22px}
.footer-brand .brand-name{font-size:30px}
.footer-head{font-family:"Roboto Slab",Georgia,serif;font-size:15px;font-weight:700;color:#fff;letter-spacing:.5px}
.contact-line{left:403px;display:flex;align-items:flex-start;gap:14px;font-size:11px;line-height:16px;color:#e8e8e8}
.contact-line svg{flex:none;margin-top:1px}
.newsletter-text{left:652px;top:76px;width:220px;font-size:11px;line-height:20px}
.email-input{left:652px;top:134px;width:207px;height:32px;background:#fff;color:#888;font-size:11px;padding:0 14px;display:flex;align-items:center}
.btn-subscribe{left:652px;top:181px;width:81px;height:25px;background:var(--red);color:#fff;font-size:10px;font-weight:600;display:flex;align-items:center;justify-content:center}
.follow-text{left:906px;top:82px;width:220px;font-size:11px;line-height:19px}
.social{top:153px;width:38px;height:38px;border:1.5px solid #fff;border-radius:50%}
.footer-rule{left:87px;top:237px;width:1026px;height:1px;background:#333}
.copyright{left:0;top:262px;width:1200px;text-align:center;font-size:12px;color:#e8e8e8}
</style>
</head>
<body>

<header class="site-header abs">
  <div class="brand abs"><span class="brand-mark"></span><span class="brand-name">VASKO LUMEN</span></div>
  <nav class="main-nav abs">
    <a class="active" style="left:556px">HOME</a>
    <a style="left:647px">ABOUT US</a>
    <a style="left:760px">VIDEO</a>
    <a style="left:851px">ALBUM</a>
    <a style="left:950px">NEWS</a>
    <a style="left:1037px">CONTACT US</a>
  </nav>
</header>

<section class="hero abs">
  <div class="hero-art abs" role="img" aria-label="Hero artwork: a hip hop artist with raised hands in a dark jungle beside two black panthers"></div>
  <h1 class="hero-title abs">Rio Vance The Sovereign</h1>
  <div class="hero-arrow abs" style="left:24px">
    <svg width="14" height="18" viewBox="0 0 14 18"><path d="M10 2 L3 9 L10 16" fill="none" stroke="#fff" stroke-width="3"/></svg>
  </div>
  <div class="hero-arrow abs" style="left:1122px">
    <svg width="14" height="18" viewBox="0 0 14 18"><path d="M4 2 L11 9 L4 16" fill="none" stroke="#fff" stroke-width="3"/></svg>
  </div>
</section>

<section class="welcome">
  <h2 class="welcome-title abs slab">Welcome to <span>Vasko Lumen</span></h2>
  <p class="welcome-sub abs">Sed ut perspiciatis unde omnis iste natus error sit voluptatem accusantium doloremque laudantium, totam rem aperiam</p>

  <div class="service abs" style="left:84px;top:903px">
    <div class="service-icon">
      <svg width="40" height="40" viewBox="0 0 40 40"><path d="M15 30 V10 L32 6 V26" fill="none" stroke="#fff" stroke-width="3"/><circle cx="11" cy="30" r="5" fill="#fff"/><circle cx="28" cy="26" r="5" fill="#fff"/></svg>
    </div>
    <h3 class="service-name">Music</h3>
    <p class="service-text">Sed ut perspiciatis unde omnis iste natus error sit voluptatem accusantium doloremque laudantium, beatae vitae dicta sunt explicabo.</p>
  </div>
  <div class="service abs" style="left:432px;top:903px">
    <div class="service-icon is-red">
      <svg width="40" height="40" viewBox="0 0 40 40"><rect x="5" y="8" width="30" height="27" rx="2" fill="none" stroke="#fff" stroke-width="3"/><line x1="5" y1="15" x2="35" y2="15" stroke="#fff" stroke-width="3"/><line x1="12" y1="4" x2="12" y2="11" stroke="#fff" stroke-width="3"/><line x1="28" y1="4" x2="28" y2="11" stroke="#fff" stroke-width="3"/><g fill="#fff"><rect x="10" y="19" width="4" height="4"/><rect x="18" y="19" width="4" height="4"/><rect x="26" y="19" width="4" height="4"/><rect x="10" y="26" width="4" height="4"/><rect x="18" y="26" width="4" height="4"/><rect x="26" y="26" width="4" height="4"/></g></svg>
    </div>
    <h3 class="service-name is-red">Events</h3>
    <p class="service-text">Sed ut perspiciatis unde omnis iste natus error sit voluptatem accusantium doloremque laudantium, beatae vitae dicta sunt explicabo.</p>
  </div>
  <div class="service abs" style="left:781px;top:903px">
    <div class="service-icon">
      <svg width="36" height="36" viewBox="0 0 36 36"><circle cx="18" cy="18" r="15" fill="#fff"/><path d="M10 10 Q14 14 12 19 Q17 21 15 27 M22 6 Q20 12 25 14 Q29 18 27 24" fill="none" stroke="#6b6b6b" stroke-width="2.5"/></svg>
    </div>
    <h3 class="service-name">Networking</h3>
    <p class="service-text">Sed ut perspiciatis unde omnis iste natus error sit voluptatem accusantium doloremque laudantium, beatae vitae dicta sunt explicabo.</p>
  </div>
</section>

<section class="studio abs">
  <h2 class="section-title abs" style="left:85px;top:28px">Recording <span>Studio</span></h2>
  <div class="mini-arrow abs" style="left:1048px;top:30px"><svg width="8" height="12" viewBox="0 0 8 12"><path d="M6 1 L2 6 L6 11" fill="none" stroke="#bbb" stroke-width="1.5"/></svg></div>
  <div class="mini-arrow abs" style="left:1082px;top:30px"><svg width="8" height="12" viewBox="0 0 8 12"><path d="M2 1 L6 6 L2 11" fill="none" stroke="#bbb" stroke-width="1.5"/></svg></div>
</section>

<article class="session abs" style="top:1274px">
  <div class="session-date abs"><div class="session-day">19</div><div class="session-month">FEB- 2017</div></div>
  <div class="divider-v abs" style="left:128px"></div>
  <div class="session-thumb abs" role="img" aria-label="Photo of artists at a recording session"></div>
  <h3 class="session-title abs">Sed ut perspiciatis unde</h3>
  <p class="session-text abs">Sed ut perspiciatis unde omnis iste beatae vitae dicta sunt explicabo.</p>
  <div class="divider-v abs" style="left:491px"></div>
  <svg class="wave abs" width="180" height="50" viewBox="0 0 180 50" aria-hidden="true"><g stroke="#8a8a8a" stroke-width="1.5">
    <line x1="10" y1="24" x2="10" y2="26"/><line x1="16" y1="22" x2="16" y2="28"/><line x1="22" y1="20" x2="22" y2="30"/><line x1="28" y1="17" x2="28" y2="33"/><line x1="34" y1="21" x2="34" y2="29"/><line x1="40" y1="14" x2="40" y2="36"/><line x1="46" y1="18" x2="46" y2="32"/><line x1="52" y1="10" x2="52" y2="40"/><line x1="58" y1="15" x2="58" y2="35"/><line x1="64" y1="8" x2="64" y2="42"/><line x1="70" y1="13" x2="70" y2="37"/><line x1="76" y1="6" x2="76" y2="44"/><line x1="82" y1="12" x2="82" y2="38"/><line x1="88" y1="9" x2="88" y2="41"/><line x1="94" y1="15" x2="94" y2="35"/><line x1="100" y1="11" x2="100" y2="39"/><line x1="106" y1="17" x2="106" y2="33"/><line x1="112" y1="14" x2="112" y2="36"/><line x1="118" y1="19" x2="118" y2="31"/><line x1="124" y1="16" x2="124" y2="34"/><line x1="130" y1="21" x2="130" y2="29"/><line x1="136" y1="19" x2="136" y2="31"/><line x1="142" y1="22" x2="142" y2="28"/><line x1="148" y1="23" x2="148" y2="27"/><line x1="154" y1="24" x2="154" y2="26"/><line x1="160" y1="24" x2="160" y2="26"/></g></svg>
  <div class="divider-v abs" style="left:768px"></div>
  <div class="ticket-label abs">TICKET</div>
  <div class="ticket-price abs">$135</div>
  <div class="btn-details abs">VIEW DETAILS</div>
</article>

<article class="session abs" style="top:1453px">
  <div class="session-date abs"><div class="session-day">19</div><div class="session-month">FEB- 2017</div></div>
  <div class="divider-v abs" style="left:128px"></div>
  <div class="session-thumb abs" role="img" aria-label="Photo of artists posing together at an event" style="background:linear-gradient(135deg,#2a4a8a,#6a4a3a 55%,#c8a070)"></div>
  <h3 class="session-title abs">Sed ut perspiciatis unde</h3>
  <p class="session-text abs">Sed ut perspiciatis unde omnis iste beatae vitae dicta sunt explicabo.</p>
  <div class="divider-v abs" style="left:491px"></div>
  <svg class="wave abs" width="180" height="50" viewBox="0 0 180 50" aria-hidden="true"><g stroke="#8a8a8a" stroke-width="1.5">
    <line x1="10" y1="24" x2="10" y2="26"/><line x1="16" y1="23" x2="16" y2="27"/><line x1="22" y1="21" x2="22" y2="29"/><line x1="28" y1="18" x2="28" y2="32"/><line x1="34" y1="15" x2="34" y2="35"/><line x1="40" y1="19" x2="40" y2="31"/><line x1="46" y1="11" x2="46" y2="39"/><line x1="52" y1="16" x2="52" y2="34"/><line x1="58" y1="7" x2="58" y2="43"/><line x1="64" y1="13" x2="64" y2="37"/><line x1="70" y1="5" x2="70" y2="45"/><line x1="76" y1="12" x2="76" y2="38"/><line x1="82" y1="8" x2="82" y2="42"/><line x1="88" y1="14" x2="88" y2="36"/><line x1="94" y1="10" x2="94" y2="40"/><line x1="100" y1="16" x2="100" y2="34"/><line x1="106" y1="13" x2="106" y2="37"/><line x1="112" y1="18" x2="112" y2="32"/><line x1="118" y1="15" x2="118" y2="35"/><line x1="124" y1="20" x2="124" y2="30"/><line x1="130" y1="18" x2="130" y2="32"/><line x1="136" y1="22" x2="136" y2="28"/><line x1="142" y1="21" x2="142" y2="29"/><line x1="148" y1="23" x2="148" y2="27"/><line x1="154" y1="24" x2="154" y2="26"/><line x1="160" y1="24" x2="160" y2="26"/></g></svg>
  <div class="divider-v abs" style="left:768px"></div>
  <div class="ticket-label abs">TICKET</div>
  <div class="ticket-price abs">$135</div>
  <div class="btn-details abs">VIEW DETAILS</div>
</article>

<section class="promo abs" role="img" aria-label="Background photo of a performer on stage holding a microphone in warm low light">
  <h2 class="promo-title abs">New music it's mainly Hiphop Based Music</h2>
  <p class="promo-text abs">Sed ut perspiciatis unde omnis iste natus error sit voluptatem accusantium doloremque laudantium, totam rem aperiam, eaque ipsa quae ab illo inventore veritatis et quasi architecto beatae vitae dicta sunt explicabo.</p>
  <div class="btn-outline abs">Click Here For More Info</div>
</section>

<section class="featured">
  <h2 class="section-title abs" style="left:85px;top:2032px">Featured <span>Video</span></h2>
  <p class="video-copy abs" style="top:2088px">Sed ut perspiciatis unde omnis iste natus error sit voluptatem accusantium doloremque laudantium, totam rem aperiam, eaque ipsa quae ab illo inventore veritatis et quasi architecto beatae vitae dicta sunt explicabo. Nemo enim ipsam voluptatem quia voluptas sit aspernatur aut odit aut fugit, sed quia consequuntur magni dolores eos qui ratione voluptatem sequi nesciunt.</p>
  <p class="video-copy abs" style="top:2228px">Nemo enim ipsam voluptatem quia vol uptas sit aspernatur aut odit aut fugit, sed qui consequuntur magni dolores eos qui ratione voluptatem sequi nesciunt.</p>
  <div class="btn-red abs">WATCH VIDEO</div>
  <div class="video-frame abs" role="img" aria-label="Video still of performers on a small stage in a warmly lit room">
    <div class="play abs"><svg width="18" height="20" viewBox="0 0 18 20"><path d="M2 1 L17 10 L2 19 Z" fill="#fff"/></svg></div>
  </div>
</section>

<section class="partners abs" aria-label="Partners">
  <div class="partner abs" style="left:87px"><span class="partner-shape"></span></div>
  <div class="partner abs" style="left:264px"><span class="partner-shape"></span></div>
  <div class="partner abs" style="left:441px"><span class="partner-shape"></span></div>
  <div class="partner abs" style="left:618px"><span class="partner-shape"></span></div>
  <div class="partner abs" style="left:795px"><span class="partner-shape"></span></div>
  <div class="partner abs" style="left:972px"><span class="partner-shape"></span></div>
</section>

<footer class="site-footer abs">
  <div class="footer-brand abs"><span class="brand-mark"></span><span class="brand-name">VASKO LUMEN</span></div>

  <h4 class="footer-head abs" style="left:403px;top:36px">CONTACT US</h4>
  <div class="contact-line abs" style="top:82px">
    <svg width="14" height="12" viewBox="0 0 14 12"><path d="M1 4 Q7 -1 13 4 L11 6 L9 4 L5 4 L3 6 Z" fill="#fff"/><rect x="3" y="7" width="8" height="5" fill="#fff"/></svg>
    <span>(000)-121-1231 (Phone)</span></div>
  <div class="contact-line abs" style="top:111px">
    <svg width="14" height="13" viewBox="0 0 14 13"><rect x="3" y="0" width="8" height="4" fill="#fff"/><rect x="0" y="4" width="14" height="6" fill="#fff"/><rect x="3" y="8" width="8" height="5" fill="#fff" stroke="#1c1c1c"/></svg>
    <span>(000)-121-1231 (Fax)</span></div>
  <div class="contact-line abs" style="top:141px">
    <svg width="14" height="11" viewBox="0 0 14 11"><rect x=".5" y=".5" width="13" height="10" fill="none" stroke="#fff"/><path d="M1 1 L7 6 L13 1" fill="none" stroke="#fff"/></svg>
    <span style="text-decoration:underline">info@vaskolumen.com</span></div>
  <div class="contact-line abs" style="top:172px">
    <svg width="14" height="14" viewBox="0 0 14 14"><path d="M7 14 L2.5 7 A5 5 0 1 1 11.5 7 Z" fill="#fff"/><circle cx="7" cy="5" r="2" fill="#1c1c1c"/></svg>
    <span>Unit #2, 169Lorem IpsumDmmy<br>Text Lorem Ipsum</span></div>

  <h4 class="footer-head abs" style="left:652px;top:36px">NEWSLETTER</h4>
  <p class="newsletter-text abs">Register Your email address to get information about us</p>
  <div class="email-input abs">Email Address</div>
  <div class="btn-subscribe abs">SUBSCRIBE</div>

  <h4 class="footer-head abs" style="left:906px;top:36px">FOLLOW US</h4>
  <p class="follow-text abs">Lorem ipsum dolor sit amet, conse ctetur adipiscing elit. Nulla in purus nibh. Donec ornare</p>
  <span class="social abs" style="left:902px" aria-label="Social link"></span>
  <span class="social abs" style="left:946px" aria-label="Social link"></span>
  <span class="social abs" style="left:990px" aria-label="Social link"></span>
  <span class="social abs" style="left:1034px" aria-label="Social link"></span>
  <span class="social abs" style="left:1078px" aria-label="Social link"></span>

  <div class="footer-rule abs"></div>
  <p class="copyright abs">© 2017 Copyright Vasko Lumen All Rights Reserved</p>
</footer>

</body>
</html>
```